Brindle 48 Focus Wheel

We need a professional **framework wheel diagram** designed for our detection dog training manual.

Our business is **Brindle 48 Dog Training**, and this graphic represents our **Detection Training Model**.

Please use the **attached reference images** as a guide for the structure and layout of the wheel.

### What we need

1. **Full wheel graphic**

* Clean circular framework wheel
* Similar structure to the attached example
* Clear sections and text
* Professional training manual style
* Transparent background

2. **Individual segment pieces**

We also need the **inner sections broken into separate pieces** (like the second reference image).

This will allow us to place each section on different pages of the manual when explaining the concepts.

Each piece should look like a **slice of the wheel**.

### Style

The design should look:

• Professional
• Clean and modern
• Structured and easy to read
• Suitable for a training manual

Avoid cartoon styles or clipart.

### Colours

Please use our brand colour palette (see attached image):

* Dark navy blue
* Steel blue
* Light blue
* White
* Light grey
* Dark grey

### Files required

Final files must include:

* Vector files (AI or EPS)
* Transparent PNG
* High-resolution PDF

Please also provide **each segment exported individually**

```html
<!DOCTYPE html>
<html lang="en">
<head>
<meta charset="utf-8">
<title>Training framework wheel</title>
<link rel="stylesheet" href="https://fonts.googleapis.com/css2?family=Montserrat:wght@700&display=swap">
<style>
  :root {
    --canvas-bg: #ffffff;
    --slice-light: #a9dff7;
    --slice-mid: #8cc8ee;
    --slice-deep: #2a74c6;
    --slice-outline: #2a2561;
    --label-ink: #111111;
  }
  html, body {
    margin: 0;
    padding: 0;
    overflow: hidden;
    background: var(--canvas-bg);
  }
  .canvas {
    width: 1200px;
    height: 1200px;
    position: relative;
    overflow: hidden;
    background: var(--canvas-bg);
  }
  .framework-wheel {
    display: block;
    width: 1200px;
    height: 1200px;
  }
  .wheel-slice {
    stroke: var(--slice-outline);
    stroke-width: 4;
    stroke-linejoin: round;
    fill: url(#sliceShade);
  }
  .slice-label {
    font-family: "Montserrat", sans-serif;
    font-weight: 700;
    font-size: 19px;
    letter-spacing: 1px;
    fill: var(--label-ink);
  }
  .shade-light { stop-color: var(--slice-light); }
  .shade-mid { stop-color: var(--slice-mid); }
  .shade-deep { stop-color: var(--slice-deep); }
</style>
</head>
<body>
<main class="canvas">
  <svg class="framework-wheel" viewBox="0 0 1040 1040" role="img" aria-label="Half wheel of five labelled training framework slices">
    <defs>
      <radialGradient id="sliceShade" gradientUnits="userSpaceOnUse" cx="520" cy="722" r="432">
        <stop offset="0" class="shade-light"/>
        <stop offset="0.8" class="shade-light"/>
        <stop offset="0.91" class="shade-mid"/>
        <stop offset="1" class="shade-deep"/>
      </radialGradient>
    </defs>

    <g class="slice slice--generic-suitability">
      <path class="wheel-slice" d="M100 722 A400 400 0 0 1 163 540 L402 722 Z"/>
      <text class="slice-label" x="158" y="673">GENERIC</text>
      <text class="slice-label" x="158" y="700">SUITABILITY</text>
    </g>

    <g class="slice slice--health-wellbeing">
      <path class="wheel-slice" d="M185 510 A400 400 0 0 1 373 390 L457 720 Z"/>
      <text class="slice-label" x="257" y="500">HEALTH &amp;</text>
      <text class="slice-label" x="257" y="527">PHYSICAL</text>
      <text class="slice-label" x="257" y="554">WELLBEING</text>
    </g>

    <g class="slice slice--engagement-relationship">
      <path class="wheel-slice" d="M400 325 A420 420 0 0 1 665 353 L491 722 Z"/>
      <text class="slice-label" x="442" y="402">ENGAGEMENT</text>
      <text class="slice-label" x="442" y="429">RELATIONSHIP</text>
    </g>

    <g class="slice slice--reward-value">
      <path class="wheel-slice" d="M710 345 A400 400 0 0 1 887 503 L528 722 Z"/>
      <text class="slice-label" x="691" y="500">REWARD</text>
      <text class="slice-label" x="691" y="527">VALUE</text>
    </g>

    <g class="slice slice--arousal-regulation">
      <path class="wheel-slice" d="M889 540 A420 420 0 0 1 940 720 L590 722 Z"/>
      <text class="slice-label" x="740" y="673">AROUSAL</text>
      <text class="slice-label" x="740" y="700">REGULATION</text>
    </g>
  </svg>
</main>
</body>
</html>
```